GHalvor Busisness Card

I am an aerospace consultant and at this time only need business cards.

Industry/Entity Type

Business

Contact Information for Business Card

Halvorsen Associates,LLC
Marcus D. Halvorsen

348 Birch Meadow Drive
Hartwell AL 35612

256-555-0187 (cell)
256-555-0142 (fax)

marcushalvorsen@mailbrook.test

```html
<!DOCTYPE html>
<html lang="en">
<head>
<meta charset="utf-8">
<title>Halvorsen Associates – Business Card</title>
<link rel="stylesheet" href="https://fonts.googleapis.com/css2?family=Fira+Sans+Condensed:wght@500;600&family=Alegreya+Sans:wght@400&display=swap">
<style>
  :root {
    --page: #e6e7e8;
    --card-dark: #2d2e33;
    --card-navy: #363659;
    --glow: #4346a0;
    --band: rgba(120, 130, 210, 0.35);
    --white: #ffffff;
    --silver-1: #9a9ba0;
    --silver-2: #f2f2f4;
  }
  html, body {
    margin: 0;
    padding: 0;
    width: 1200px;
    height: 833px;
    overflow: hidden;
    background: var(--page);
  }
  .card {
    position: absolute;
    left: 117px;
    top: 122px;
    width: 966px;
    height: 589px;
    overflow: hidden;
    color: var(--white);
    background:
      radial-gradient(ellipse 420px 160px at 48% 25%, rgba(67, 70, 160, 0.75), transparent 70%),
      radial-gradient(ellipse 300px 220px at 100% 40%, rgba(80, 90, 180, 0.55), transparent 70%),
      linear-gradient(180deg, var(--card-dark) 0%, var(--card-navy) 55%, #3a3450 100%);
  }
  .band {
    position: absolute;
    left: 0;
    top: 149px;
    width: 100%;
    height: 216px;
    background: linear-gradient(90deg, rgba(110,120,200,0.45) 0%, rgba(130,135,200,0.4) 40%, rgba(90,95,170,0.3) 100%);
  }
  .rule {
    position: absolute;
    left: 0;
    top: 0;
  }
  .divider {
    position: absolute;
    left: 453px;
    top: 178px;
    width: 5px;
    height: 162px;
    background: var(--white);
  }
  .wordmark {
    position: absolute;
    left: 76px;
    top: 196px;
    margin: 0;
    font-family: "Fira Sans Condensed", sans-serif;
    font-weight: 600;
    font-size: 50px;
    line-height: 52px;
    letter-spacing: 1px;
    text-transform: uppercase;
  }
  .wordmark span { display: block; }
  .contact {
    position: absolute;
    left: 495px;
    top: 178px;
  }
  .contact-name {
    margin: 0 0 6px;
    font-family: "Fira Sans Condensed", sans-serif;
    font-weight: 500;
    font-size: 36px;
    line-height: 42px;
  }
  .contact-lines {
    margin: 0;
    font-family: "Alegreya Sans", sans-serif;
    font-size: 26px;
    line-height: 31px;
    letter-spacing: 1px;
  }
  .email {
    position: absolute;
    left: 219px;
    top: 388px;
    margin: 0;
    font-family: "Alegreya Sans", sans-serif;
    font-size: 29px;
    letter-spacing: 1.6px;
  }
</style>
</head>
<body>
  <div class="card">
    <div class="band"></div>

    <svg class="rule" width="966" height="589" viewBox="0 0 966 589" aria-hidden="true">
      <defs>
        <linearGradient id="silver" x1="0" x2="1" y1="0" y2="0">
          <stop offset="0" stop-color="var(--silver-1)"/>
          <stop offset="0.45" stop-color="var(--silver-2)"/>
          <stop offset="0.7" stop-color="var(--silver-1)"/>
          <stop offset="0.8" stop-color="#ffffff"/>
          <stop offset="1" stop-color="#ffffff"/>
        </linearGradient>
      </defs>
      <rect x="0" y="367" width="913" height="9" fill="url(#silver)"/>
      <polyline points="911,371.5 966,428" fill="none" stroke="#ffffff" stroke-width="8"/>
    </svg>

    <h1 class="wordmark"><span>Halvorsen</span><span>Associates</span></h1>

    <div class="divider"></div>

    <div class="contact">
      <p class="contact-name">LLC Marcus D. Halvorsen</p>
      <p class="contact-lines">
        348 Birch Meadow Drive Hartwell<br>
        AL 35612<br>
        Cell : 256-555-0187 ,<br>
        Fax : 256-555-0142
      </p>
    </div>

    <p class="email">Email : marcushalvorsen@mailbrook.test</p>
  </div>
</body>
</html>
```